Infectious Diseases Research Laboratory Needs Business Card

We need a business card for an academic research laboratory based in Kansas City called MORVEK. The full lab name is Microbial Dose-Response/Exposure Bridging Studies Laboratory, but this does not need to be incorporated. We study novel ways to optimize the treatment of multidrug-resistant bacterial infections ("superbugs") throughout the entire biomedical research spectrum (from benchtop to bedside). The name MORVEK is not only an acronym for our lab name, but also represents our desire to make discoveries and explore the unknown (the stars, if you well). It also serves as an ode to the state of Kansas motto where we are based, ad astra per aspera ("to the stars, through difficulty").

Target Market(s)

Pharmaceutical companies, researchers

Industry/Entity Type

Pharmaceutical

Contact Information for Business Card

The business card should incorporate and complement our new logo (see uploaded files). Double-sided designs are preferred. Looking for something modern, but professional.

Font styles to use
Sans Serif

Requirements
Must have
• Double-sided. One side would ideally be a solid color incorporating logo and the other should also have the logo (smaller), but incorporate staff information.
• Color codes:
• Red: #F04C51
• Blue: #3477B5
• Gray: #808285

```html
<!DOCTYPE html>
<html lang="en">
<head>
<meta charset="utf-8">
<title>MORVEK Business Card</title>
<link rel="stylesheet" href="https://fonts.googleapis.com/css2?family=Work+Sans:wght@400;500;600&display=swap">
<style>
  :root {
    --red: #F04C51;
    --blue: #3477B5;
    --gray: #808285;
    --card: #232323;
    --backdrop: #141414;
    --ink: #f2f2f2;
  }
  * { margin: 0; padding: 0; box-sizing: border-box; }
  html, body {
    width: 1200px; height: 900px; overflow: hidden;
    background: var(--backdrop);
    font-family: "Work Sans", sans-serif;
  }
  .canvas { position: relative; width: 1200px; height: 900px; }
  .card {
    position: absolute; left: 285px; width: 630px; height: 360px;
    background: var(--card); overflow: hidden;
  }
  .card--front { top: 70px; }
  .card--back { top: 470px; }
  .card__band {
    position: absolute; left: 0; right: 0; bottom: 0; height: 11px;
    background: var(--red);
  }

  /* front */
  .brand {
    position: absolute; top: 118px; left: 0; right: 0;
    display: flex; justify-content: center; align-items: center; gap: 22px;
  }
  .brand__dot { width: 44px; height: 44px; border-radius: 50%; background: var(--red); }
  .brand__name {
    font-size: 54px; font-weight: 400; letter-spacing: 8px; color: #bdbdbd;
  }
  .front__web {
    position: absolute; top: 282px; left: 0; right: 0; text-align: center;
    font-size: 19px; color: var(--ink); letter-spacing: 0.5px;
  }
  .front__web .accent { color: var(--blue); }

  /* back */
  .back__name {
    position: absolute; left: 42px; top: 122px; width: 265px;
    font-size: 52px; font-weight: 500; letter-spacing: 3px; color: var(--red);
    white-space: nowrap;
  }
  .back__divider {
    position: absolute; left: 330px; top: 95px; width: 1.5px; height: 150px;
    background: var(--blue);
  }
  .staff { position: absolute; left: 358px; top: 95px; }
  .staff__name { font-size: 26px; font-weight: 500; color: var(--red); }
  .staff__role { font-size: 18px; color: var(--ink); margin-top: 2px; }
  .contacts { list-style: none; margin-top: 16px; }
  .contacts li {
    display: flex; align-items: center; gap: 12px;
    font-size: 17px; color: var(--ink); line-height: 27px;
  }
  .contacts svg { width: 16px; height: 16px; flex: none; }
  .back__address {
    position: absolute; left: 0; right: 0; top: 300px; text-align: center;
    font-size: 18px; color: var(--ink); letter-spacing: 0.5px;
  }
</style>
</head>
<body>
<main class="canvas">
  <section class="card card--front" aria-label="Card front">
    <div class="brand">
      <span class="brand__dot"></span>
      <span class="brand__name">MORVEK</span>
    </div>
    <p class="front__web">www.<span class="accent">morvek</span>.com</p>
    <div class="card__band"></div>
  </section>

  <section class="card card--back" aria-label="Card back">
    <p class="back__name">MORVEK</p>
    <div class="back__divider"></div>
    <div class="staff">
      <p class="staff__name">Dana Whitcombe</p>
      <p class="staff__role">Founder</p>
      <ul class="contacts">
        <li>
          <svg viewBox="0 0 16 16" aria-hidden="true"><rect x="4" y="1" width="8" height="14" rx="1.5" fill="none" stroke="#F04C51" stroke-width="1.4"/><line x1="7" y1="12.5" x2="9" y2="12.5" stroke="#F04C51" stroke-width="1.2"/></svg>
          (555) 018-4427
        </li>
        <li>
          <svg viewBox="0 0 16 16" aria-hidden="true"><rect x="1" y="3.5" width="14" height="9" fill="#F04C51"/><polyline points="1,3.5 8,9 15,3.5" fill="none" stroke="#232323" stroke-width="1.2"/></svg>
          info@danawhitcombe.com
        </li>
        <li>
          <svg viewBox="0 0 16 16" aria-hidden="true"><g fill="none" stroke="#F04C51" stroke-width="1.2"><circle cx="8" cy="8" r="6.5"/><ellipse cx="8" cy="8" rx="3" ry="6.5"/><line x1="1.5" y1="8" x2="14.5" y2="8"/><line x1="2.5" y1="4.8" x2="13.5" y2="4.8"/><line x1="2.5" y1="11.2" x2="13.5" y2="11.2"/></g></svg>
          www.morvek.org
        </li>
      </ul>
    </div>
    <p class="back__address">240 Linden Ave Fairhollow, KS 66012</p>
    <div class="card__band"></div>
  </section>
</main>
</body>
</html>
```